Website Design for a different kind of Business Consulting organisation needed!

We need a website design that reflects who we are, the simplicity of our consulting business and with a focus on our priority - to help our clients deliver, or execute - the "e" in Vantor-o.

Our key high level requirements are:
1) Simple and intuitive look and feel
2) Integration with all key social media platforms, chirpline, friendwall, workmesh, blogvine.

10 pages, tops.
- Main page - Welcome
- About Us/ Who are Vantor-o?
- 5 services pages - Project Management, Business Process Management, Change Management, Business Analysis and Finance Systems
- Contact Us

Something like:
http://www.hlmworks.example/

Vantor-o is a registered trademark and all Logos and other branded material are attached for reference.

So, what’s our gig: A few snippets from previous work...

We are a different kind of business consulting group. We partner with our clients to help them deliver change. We don't just provide them with the theory. We also provide them with the leadership and capability to execute the change.

We aren’t a one stop shop, and we don’t offer cookie cutter solutions. We’re a boutique consulting firm covering Project Management, Business Process Management, Change Management and Business Analytics.

Vantor-o is a professional services organisation that partners with their clients to lead the execution of strategic process and system improvement initiatives. Vantor-o combines hands on delivery with coaching in best practice methodologies and approaches to build their clients capabilities to ensure their ongoing success in project implementations.

UPDATES:

Thanks to everyone who has submitted designs so far. The standard of designs coming through is quite high, with lots of professional designs that nail the design brief. Eliminating them is proving to be quite challenging.

A few updates to the job brief:
- Please make sure the design fits on one page. We would like all of our information to be on the first page that people see without them having to scroll down
- Please ensure you include the FIVE services we offer in the design
- Please use corporate images/snapvault photos in your designs which are relevant to our business
- Please add a section for a live chirpline feed from our chirpline account and a link to circlenet+
- Please add a section for news/updates

Also, if you are able to build a site once a design is selected, please let us know.

Thanks,

Marisol.

Target Market(s)

Our target customers are large enterprises in Australia that are growing rapidly and have recently (last 24 months) undertaken or are currently undergoing software implementations and business process improvement programs. These businesses have a turnover of $100m or above and are working hard to differentiate themselves from their competitors but are not seeing the return on investment promised by software vendors and process improvement initiatives.

Industry/Entity Type

Leadership

Requirements
Must have
• Collaboration / Training / Workshop / Consulting images all of a professional nature.
Simple, non-cluttered look with plenty of white space.

```html
<!DOCTYPE html>
<html lang="en">
<head>
<meta charset="utf-8">
<title>Vantor-o Pty Ltd — Business Consulting</title>
<link rel="stylesheet" href="https://fonts.googleapis.com/css2?family=Lato:wght@400;700&family=Open+Sans:wght@400;600;700&display=swap">
<style>
:root{
  --brand:#1b509c;
  --band:#24509a;
  --ink:#222;
  --muted:#7a7a7a;
  --rule:#e2e2e2;
  --frame:#f5f5f5;
}
*{box-sizing:border-box;margin:0;padding:0}
html,body{width:1043px;height:1200px;overflow:hidden;background:#fff}
body{position:relative;font-family:'Lato',sans-serif;color:var(--ink)}
.abs{position:absolute}
a{color:inherit;text-decoration:none}

/* top bar */
.topbar{left:0;top:0;width:1043px;height:28px;border-bottom:1px solid var(--rule)}
.contact{top:8px;font-size:10px;color:var(--muted);display:flex;align-items:center;gap:6px}
.contact svg{display:block}
.social{right:154px;top:6px;display:flex;gap:8px}
.social span{width:17px;height:17px;border-radius:50%;background:#b9b9b9;display:block}
.social span.on{background:var(--brand)}

/* header */
.header-rule{left:0;top:106px;width:1043px;height:1px;background:var(--rule)}
.logo{left:132px;top:42px;color:var(--brand);font-size:40px;font-weight:400;letter-spacing:1px;line-height:1}
.logo-sub{left:232px;top:78px;color:var(--brand);font-size:6px}
.nav{left:392px;top:61px;display:flex;gap:13px;font-size:12px;color:#555}
.nav a.current{color:var(--brand)}
.search{left:751px;top:56px;width:160px;height:25px;border:1px solid #ccc;font-size:10px;color:#999;padding:7px 8px}
.search svg{position:absolute;right:8px;top:6px}

/* hero */
.hero{left:132px;top:115px;width:779px;height:331px;border:1px solid #ddd;background:var(--frame)}
.hero-photo{left:141px;top:123px;width:762px;height:315px;background:linear-gradient(90deg,#e9e4df 0%,#c9ccd2 35%,#f0ece8 60%,#d9d4cf 100%)}

/* features */
.feature{top:476px;width:245px;height:90px}
.feature .badge{position:absolute;left:0;top:0;width:56px;height:56px;border-radius:50%;border:2px solid var(--brand);padding:3px}
.feature .badge div{width:100%;height:100%;border-radius:50%;background:var(--brand);display:flex;align-items:center;justify-content:center}
.feature h3{position:absolute;left:67px;top:0;font-size:16px;font-weight:400;color:var(--ink);white-space:nowrap}
.feature h3.accent{color:var(--brand)}
.feature p{position:absolute;left:67px;top:20px;width:185px;font-size:10.5px;line-height:16.5px;color:var(--muted)}
.feature .more{position:absolute;left:67px;top:71px;font-size:10px;color:var(--ink)}
.feature .more.accent{color:var(--brand)}

.rule{left:132px;width:779px;height:1px;background:var(--rule)}

/* services */
.service{top:628px;width:182px}
.service .photo{width:182px;height:125px}
.service .label{margin-top:4px;height:25px;background:var(--band);color:#fff;font-size:9.5px;font-weight:700;display:flex;align-items:center;justify-content:center}

/* welcome */
.welcome h2{font-family:'Open Sans',sans-serif;font-weight:600;font-size:25px;color:var(--ink);white-space:nowrap}
.welcome h2 b{color:var(--brand);font-weight:700;font-size:28px}
.welcome p{font-family:'Open Sans',sans-serif;width:510px;font-size:10.6px;line-height:18.2px;color:var(--muted)}
.btn{left:134px;top:1057px;width:83px;height:25px;border:1px solid var(--brand);color:var(--brand);font-family:'Open Sans',sans-serif;font-size:10px;display:flex;align-items:center;justify-content:center}

/* news */
.news-title{left:662px;top:850px;font-family:'Open Sans',sans-serif;font-size:20px;font-weight:400;color:var(--ink)}
.news-item{left:662px;width:249px;border-bottom:1px solid #ccc}
.news-item .thumb{position:absolute;left:0;top:0;width:67px;height:65px}
.news-item h4{position:absolute;left:81px;top:-2px;font-size:12px;font-weight:400;color:var(--ink);white-space:nowrap}
.news-item h4.accent{color:var(--brand)}
.news-item time{position:absolute;left:81px;top:17px;font-size:8px;color:var(--ink)}
.news-item p{position:absolute;left:82px;top:33px;width:160px;font-size:9.5px;line-height:15px;color:var(--muted)}

/* footer */
.foot-logo{left:132px;top:1128px;color:var(--brand);font-size:26px;letter-spacing:.5px;line-height:1}
.foot-nav{right:133px;top:1135px;display:flex;gap:10px;font-size:9.5px;color:#333}
.band{left:0;top:1172px;width:1043px;height:28px;background:var(--band);color:#fff;font-size:10px;padding:8px 0 0 133px}
</style>
</head>
<body>

<div class="abs topbar"></div>
<div class="abs contact" style="left:134px">
  <svg width="14" height="10" viewBox="0 0 14 10"><rect x="0.5" y="0.5" width="13" height="9" fill="#aaa"/><path d="M0.5 0.5 7 5.5 13.5 0.5" fill="none" stroke="#fff" stroke-width="1"/></svg>
  jordan.pell@vantor-o.example
</div>
<div class="abs contact" style="left:298px">
  <svg width="8" height="13" viewBox="0 0 8 13"><rect x="0.5" y="0.5" width="7" height="12" rx="1" fill="none" stroke="#aaa"/><rect x="3" y="10" width="2" height="1" fill="#aaa"/></svg>
  + 61 400 555 018
</div>
<div class="abs social" aria-label="Social links: friendwall, chirpline, workmesh">
  <span class="on"></span><span></span><span></span>
</div>

<div class="abs logo">Vantor-o</div>
<div class="abs logo-sub">Pty Ltd</div>

<nav class="abs nav">
  <a class="current">Home</a><a>About Us</a><a>Services</a><a>Our Clients</a><a>Blog</a><a>Contact Us</a>
</nav>
<div class="abs search">Search
  <svg width="12" height="12" viewBox="0 0 12 12"><circle cx="5" cy="5" r="3.8" fill="none" stroke="#999" stroke-width="1.5"/><path d="M8 8l3 3" stroke="#999" stroke-width="1.8"/></svg>
</div>
<div class="abs header-rule"></div>

<div class="abs hero"></div>
<div class="abs hero-photo" role="img" aria-label="Smiling businesswoman in front of colleagues at a meeting table"></div>

<section class="abs feature" style="left:133px">
  <div class="badge"><div>
    <svg width="22" height="22" viewBox="0 0 22 22" fill="none" stroke="#fff" stroke-width="2"><circle cx="11" cy="11" r="9" fill="#fff" stroke="none"/><path d="M4 8c5 1 9 4 10 12M8 2.5c1 5 6 8 12 8" stroke="#1b509c"/></svg>
  </div></div>
  <h3 class="accent">What we do</h3>
  <p>Lorem Ipsum is simply dummy text of the printing and typesetting industry. Lorem Ipsum .</p>
  <a class="more accent">Read More &nbsp;›</a>
</section>
<section class="abs feature" style="left:398px">
  <div class="badge"><div>
    <svg width="22" height="22" viewBox="0 0 22 22"><path d="M19 3c-6 0-10 4-12 9l3 3c5-2 9-6 9-12z" fill="#fff"/><path d="M6 13l-3 1 3-5h3zM9 16l-1 3 5-3v-3z" fill="#fff"/><circle cx="14" cy="8" r="1.6" fill="#1b509c"/></svg>
  </div></div>
  <h3>Our Expertise</h3>
  <p>Lorem Ipsum is simply dummy text of the printing and typesetting industry. Lorem Ipsum .</p>
  <a class="more">Read More &nbsp;›</a>
</section>
<section class="abs feature" style="left:663px">
  <div class="badge"><div>
    <svg width="22" height="22" viewBox="0 0 22 22"><path d="M6 4h12l-2 12H4z" fill="#fff"/><path d="M4 16h12l-1 3H3z" fill="#fff" opacity=".7"/></svg>
  </div></div>
  <h3>Case Studies</h3>
  <p>Lorem Ipsum is simply dummy text of the printing and typesetting industry. Lorem Ipsum .</p>
  <a class="more">Read More &nbsp;›</a>
</section>

<div class="abs rule" style="top:590px"></div>

<div class="abs service" style="left:132px">
  <div class="photo" role="img" aria-label="Woman reviewing documents at a laptop in a kitchen" style="background:linear-gradient(135deg,#bdb5a6,#ece8e1 55%,#8a8377)"></div>
  <div class="label">Project Manamement</div>
</div>
<div class="abs service" style="left:331px">
  <div class="photo" role="img" aria-label="Two colleagues discussing papers at a desk" style="background:linear-gradient(135deg,#e8eaee,#3a3f4a 45%,#f2f2f2)"></div>
  <div class="label">Business Process Manamement</div>
</div>
<div class="abs service" style="left:530px">
  <div class="photo" role="img" aria-label="Businesswoman in a dark suit in a bright office" style="background:linear-gradient(135deg,#c8d3d8,#e6e0d8 50%,#2b2b30)"></div>
  <div class="label">Change Manamement</div>
</div>
<div class="abs service" style="left:729px">
  <div class="photo" role="img" aria-label="Woman beside a bar chart with a highlighted column" style="background:linear-gradient(90deg,#4a3a30,#f3f6fa 35%,#8fd6f3 75%,#fff)"></div>
  <div class="label">Business Analytics</div>
</div>

<div class="abs rule" style="top:818px"></div>

<section class="welcome">
  <h2 class="abs" style="left:134px;top:848px">Welcome to <b>Vantor- o</b></h2>
  <p class="abs" style="left:134px;top:896px">Contrary to popular belief, Lorem Ipsum is not simply random text. It has roots in a piece of classical Latin literature from 45 BC, making it over 2000 years old. Edwin Harrowgate, a Latin professor at Greyvale-Marsh College in Virginia, looked up one of the more obscure Latin words, consectetur, from a Lorem Ipsum passage, and going through the cites of the word in classical literature, discovered the undoubtable source.</p>
  <p class="abs" style="left:134px;top:1005px">Lorem Ipsum passage, and going through the cites of the word in classical literature, discovered the undoubtable source.</p>
  <a class="abs btn">Read more</a>
</section>

<h2 class="abs news-title">Latest News</h2>
<article class="abs news-item" style="top:897px;height:80px">
  <div class="thumb" role="img" aria-label="Business people racing to a finish line" style="background:linear-gradient(180deg,#6f9a4a,#b08a7c 50%,#3b3b3b)"></div>
  <h4>Lorem Ipsum Simply Dummy</h4>
  <time>19 March 2014, 20:30</time>
  <p>Lorem Ipsum has been the industry's standard dummy text</p>
</article>
<article class="abs news-item" style="top:999px;height:78px">
  <div class="thumb" role="img" aria-label="Businesswoman seated at an office desk" style="background:linear-gradient(135deg,#f1d9c8,#3a2a26 55%,#e8e2dc)"></div>
  <h4 class="accent">Lorem Ipsum Simply Dummy</h4>
  <time>17 Feb 2014, 20:30</time>
  <p>Lorem Ipsum has been the industry's standard dummy text</p>
</article>

<div class="abs rule" style="top:1116px"></div>
<div class="abs foot-logo">Vantor-o</div>
<nav class="abs foot-nav"><a>Home</a><a>About</a><a>News</a><a>Privacy Policy</a><a>Contact Us</a></nav>
<footer class="abs band">Vantor - o © 2014 all rights Reserved</footer>

</body>
</html>
```